Tarrow Creek plumbing plumbing company business card design

Something sinilar to business card i upload it is my old business card design
And have a good watermark with the logo or majority of the logot in rhe background as watermark

Plumbing business similar to uploaded design with a nice watermark of the logo

Font styles to use
Script

Colors

Designer to choose colors to be used in the design.

```html
<!DOCTYPE html>
<html lang="en">
<head>
<meta charset="utf-8">
<title>Tarrow Creek Plumbing – Business Card</title>
<link rel="stylesheet" href="https://fonts.googleapis.com/css2?family=Lato:ital,wght@0,400;0,700;1,400&family=Montserrat:wght@500;700&display=swap">
<style>
  :root {
    --brand-blue: #1372b9;
    --accent-blue: #0a78c2;
    --ink: #111111;
    --card-white: #ffffff;
    --backdrop: #e8e6e2;
    --watermark-light: #eef1f4;
    --watermark-blue: #2a82c3;
  }
  * { margin: 0; padding: 0; box-sizing: border-box; }
  html, body { width: 900px; height: 1200px; overflow: hidden; }
  body { background: var(--backdrop); position: relative; font-family: "Lato", sans-serif; color: var(--ink); }

  .card { position: absolute; left: 86px; width: 735px; height: 430px; overflow: hidden; box-shadow: 0 4px 10px rgba(0,0,0,0.25); }
  .card--front { top: 137px; background: var(--card-white); }
  .card--back { top: 633px; background: var(--brand-blue); }

  .watermark { position: absolute; border-radius: 50%; }
  .card--front .watermark { right: 40px; top: 170px; width: 230px; height: 230px; background: var(--watermark-light); }
  .card--back .watermark { left: 0; top: 60px; width: 320px; height: 320px; background: var(--watermark-blue); opacity: 0.6; }

  .brand-name { position: absolute; font-family: "Montserrat", sans-serif; font-weight: 700; letter-spacing: 0.12em; text-transform: uppercase; white-space: nowrap; }
  .card--front .brand-name { right: 54px; top: 80px; font-size: 20px; color: var(--ink); display: flex; align-items: center; gap: 10px; }
  .brand-mark { width: 16px; height: 16px; background: var(--accent-blue); }
  .card--back .brand-name { left: 0; right: 0; top: 180px; text-align: center; font-size: 32px; color: var(--card-white); }

  .holder { position: absolute; left: 52px; top: 218px; }
  .holder__name { font-size: 31px; font-weight: 700; line-height: 1; }
  .holder__first { color: var(--accent-blue); }
  .holder__role { font-size: 17px; margin-top: 8px; }

  .contacts { position: absolute; left: 52px; top: 304px; list-style: none; }
  .contacts li { display: flex; align-items: center; gap: 11px; font-size: 17px; height: 29px; }
  .contacts svg { width: 13px; height: 13px; fill: var(--accent-blue); }

  .licence { position: absolute; right: 52px; top: 362px; font-size: 17px; font-style: italic; }

  .stripe { position: absolute; bottom: 0; height: 15px; }
  .stripe--blue { left: 0; width: 424px; background: var(--accent-blue); }
  .stripe--black { left: 432px; right: 0; background: var(--ink); }

  .back-web { position: absolute; left: 0; right: 0; top: 371px; text-align: center; font-size: 17px; letter-spacing: 0.06em; color: var(--card-white); }
</style>
</head>
<body>
  <section class="card card--front" aria-label="Card front">
    <div class="watermark" aria-hidden="true"></div>
    <div class="brand-name"><span class="brand-mark"></span>Tarrow Creek Plumbing</div>

    <div class="holder">
      <p class="holder__name"><span class="holder__first">Daniel</span> Marsh</p>
      <p class="holder__role">Director</p>
    </div>

    <ul class="contacts">
      <li>
        <svg viewBox="0 0 24 24" aria-hidden="true"><path d="M6.6 10.8a15.2 15.2 0 0 0 6.6 6.6l2.2-2.2c.3-.3.7-.4 1-.2 1.1.4 2.3.6 3.6.6.6 0 1 .4 1 1V20c0 .6-.4 1-1 1A17 17 0 0 1 3 4c0-.6.4-1 1-1h3.5c.6 0 1 .4 1 1 0 1.3.2 2.5.6 3.6.1.3 0 .7-.2 1z"/></svg>
        0400 555 019
      </li>
      <li>
        <svg viewBox="0 0 24 24" aria-hidden="true"><path d="M2 5h20v2l-10 6L2 7z M2 9l10 6 10-6v10H2z"/></svg>
        info@tarrowcreekplumbing.com
      </li>
      <li>
        <svg viewBox="0 0 24 24" aria-hidden="true"><path d="M12 2a10 10 0 1 0 0 20 10 10 0 0 0 0-20zm6.9 9h-3a15 15 0 0 0-1.3-5.8A8 8 0 0 1 18.9 11zM12 4c.9 1.2 1.8 3.6 1.9 7h-3.8c.1-3.4 1-5.8 1.9-7zM9.4 5.2A15 15 0 0 0 8.1 11h-3a8 8 0 0 1 4.3-5.8zM5.1 13h3a15 15 0 0 0 1.3 5.8A8 8 0 0 1 5.1 13zM12 20c-.9-1.2-1.8-3.6-1.9-7h3.8c-.1 3.4-1 5.8-1.9 7zm2.6-1.2a15 15 0 0 0 1.3-5.8h3a8 8 0 0 1-4.3 5.8z"/></svg>
        www.tarrowcreekplumbing.com.au
      </li>
    </ul>

    <p class="licence">Lic No.480217c</p>

    <div class="stripe stripe--blue"></div>
    <div class="stripe stripe--black"></div>
  </section>

  <section class="card card--back" aria-label="Card back">
    <div class="watermark" aria-hidden="true"></div>
    <div class="brand-name">Tarrow Creek Plumbing</div>
    <p class="back-web">www.tarrowcreekplumbing.com.au</p>
  </section>
</body>
</html>
```